Business Card And Stationary Set for : Pintu Ravel Sdn. Bhd.
I need double sided standard sized Business Card [3.5" x 2"]
Same font or you can recommend
Professional
Ferril Wakin
41C, Jalan Cempaka Lima,
Taman Seroja,
47310 Kuala Lumpur,
Malaysia.
info@pintuvrel.com.my
www.pintuvrel.com.my
618204-K
Please put the company name and license no. above the company address. Smaller font for the license number.
Pintu Ravel Sdn. Bhd. (618204-K)
Company logo.
Specialized In: Auto Gate & Security Systems

```html
<!DOCTYPE html>
<html lang="en">
<head>
<meta charset="utf-8">
<title>Pintu Ravel Sdn. Bhd. – Business Card</title>
<link href="https://fonts.googleapis.com/css2?family=Oswald:wght@600&family=Open+Sans:wght@400;600;700&display=swap" rel="stylesheet">
<style>
  :root{
    --bg:#e9e7e4;
    --card:#ffffff;
    --ink:#111111;
    --orange:#f7931e;
    --grey:#6d6e71;
    --line:#d7d7d7;
  }
  *{margin:0;padding:0;box-sizing:border-box}
  html,body{width:1200px;height:961px;overflow:hidden;background:var(--bg)}
  .stage{position:relative;width:1200px;height:961px}
  .card{position:absolute;width:520px;height:297px;background:var(--card);border-radius:16px;overflow:hidden;box-shadow:0 10px 28px rgba(0,0,0,.18)}
  .card--front{left:50px;top:200px}
  .card--back{left:630px;top:464px}
  .card__shapes{position:absolute;inset:0}
  .brand{position:absolute;display:flex;align-items:center;gap:10px;font-family:"Oswald",sans-serif;font-weight:600;color:var(--orange);text-transform:uppercase;letter-spacing:.5px}
  .brand__mark{background:var(--orange)}
  .card--front .brand{left:34px;top:112px;font-size:30px}
  .card--front .brand__mark{width:22px;height:22px}
  .holder{position:absolute;left:70px;top:170px;font-family:"Open Sans",sans-serif;font-weight:700;font-size:15px;color:var(--orange);letter-spacing:.6px;text-transform:uppercase}
  .contact{position:absolute;left:330px;font-family:"Open Sans",sans-serif;font-size:8.5px;color:var(--grey);line-height:1.35}
  .contact__row{display:flex;align-items:center;gap:6px}
  .contact__row svg{flex:none}
  .contact--phones{top:26px}
  .contact--address{top:120px}
  .contact--address .company{font-weight:600}
  .contact--address .license{font-size:7px}
  .contact--web{top:226px}
  .card--back .brand{left:0;right:0;top:98px;justify-content:center;font-size:44px}
  .card--back .brand__mark{width:30px;height:30px}
  .url{position:absolute;left:0;right:0;top:200px;text-align:center;font-family:"Open Sans",sans-serif;font-weight:700;font-size:15px;letter-spacing:2.4px;color:var(--orange)}
</style>
</head>
<body>
<main class="stage">
  <section class="card card--front" aria-label="Card front">
    <svg class="card__shapes" width="520" height="297" viewBox="0 0 520 297" aria-hidden="true">
      <polygon points="0,0 300,0 250,297 0,297" fill="var(--ink)"/>
      <polygon points="0,0 64,0 0,58" fill="var(--orange)"/>
      <polygon points="0,236 0,297 92,297" fill="var(--orange)"/>
      <line x1="312" y1="0" x2="262" y2="297" stroke="var(--line)" stroke-width="2"/>
    </svg>
    <div class="brand"><span class="brand__mark"></span>Pintu Ravel</div>
    <div class="holder">Ferril Wakin</div>

    <div class="contact contact--phones">
      <div class="contact__row"><svg width="9" height="9" viewBox="0 0 10 10"><path d="M2 1h2l1 2-1.2 1a6 6 0 0 0 2.2 2.2L7 5l2 1v2c0 .6-.5 1-1 1A8 8 0 0 1 1 2c0-.5.4-1 1-1z" fill="var(--grey)"/></svg>+603 7120 4455</div>
      <div class="contact__row"><svg width="9" height="9" viewBox="0 0 10 10"><rect x="2.5" y=".5" width="5" height="9" rx="1" fill="var(--grey)"/></svg>+6012 3380 617</div>
      <div class="contact__row"><svg width="9" height="9" viewBox="0 0 10 10"><rect x="1" y="3" width="8" height="6" fill="var(--grey)"/><rect x="3" y="1" width="4" height="3" fill="var(--grey)"/></svg>+603 7120 4490</div>
    </div>

    <div class="contact contact--address">
      <div class="contact__row"><svg width="9" height="11" viewBox="0 0 10 12"><path d="M5 0a4 4 0 0 1 4 4c0 3-4 8-4 8S1 7 1 4a4 4 0 0 1 4-4z" fill="var(--grey)"/><circle cx="5" cy="4" r="1.5" fill="#fff"/></svg><span class="company">Pintu Ravel Sdn. Bhd. <span class="license">(618204-K)</span></span></div>
      <div style="padding-left:15px">41C, Jalan Cempaka Lima,<br>Taman Seroja,<br>47310 Kuala Lumpur, Malaysia.</div>
    </div>

    <div class="contact contact--web">
      <div class="contact__row"><svg width="9" height="8" viewBox="0 0 10 8"><rect x=".5" y=".5" width="9" height="7" fill="none" stroke="var(--grey)"/><path d="M.5 .5 5 4.5 9.5 .5" fill="none" stroke="var(--grey)"/></svg>info@pintuvrel.com.my</div>
      <div class="contact__row"><svg width="9" height="9" viewBox="0 0 10 10"><circle cx="5" cy="5" r="4.3" fill="none" stroke="var(--grey)"/><path d="M.7 5h8.6M5 .7c-2.4 2.6-2.4 6 0 8.6M5 .7c2.4 2.6 2.4 6 0 8.6" fill="none" stroke="var(--grey)" stroke-width=".8"/></svg>www.pintuvrel.com.my</div>
    </div>
  </section>

  <section class="card card--back" aria-label="Card back">
    <div class="brand"><span class="brand__mark"></span>Pintu Ravel</div>
    <div class="url">www.pintuvrel.com.my</div>
  </section>
</main>
</body>
</html>
```